ROOFING SALES QUOTE TEMPLATE / BROCHURE

I am a roofing contractor looking to elevate and simplify the sales presentation of our roof installation services to our customers through a slick/company branded bid form or brochure. Im looking more for design elements in a template format that can be used/modified to have information populated based on unique customer needs.
I would like to have the bid form or brochure present 3 options to homeowners: GOOD / BETTER / BEST

Potentially include pages with details to educate the homeowners on the components of a roof, the material /product specifications included in each of the GOOD/BETTER/BEST options, our insurance information, licensing, etc.

For example: Homeowner Dorian is looking to have his asphalt shingle roof replaced on his residential home. Dorian knows nothing about roofing, but knows the roof is getting old.
Bramblet Roofing would like to present him with three replacement options, with different price points:
OPTION 1 (Good) = Remove and replace existing roof with new shingle tier 1 quality
OPTION 2 (BETTER) = remove and replace existing roof with new shingle tier 2 quality and better warranty
OPTION 3 (BEST) = remove and replace existing roof with new highest quality shingle and highest grade warranty

I would like one page to concisely present all three options, visually simple with price, and option summaries

One page which essentially educates on the components of a roof (attic space, trusses/rafters/eaves , plywood decking, roofing felts/underlayment, shingle material, metal flashings, ridge and hip shingles, ventilation, etc) -graphic?

One or more pages that show more specific details/scope of each of the options presented (unless this is TMI and we can provide a URL

Another page showcasing our license, insurance, bonds, certification, etc.

For branding, we are partnered with the manufacturer KLO in case we can co-brand anything.

Most of these will be used electronically and filled out as a PDF or similar.

Target Market(s)

Residential and commercial building owners looking for roof replacements

Industry/Entity Type

Roofing (USA - California)

Requirements
Must have
• present 3 options to homeowners: GOOD / BETTER / BEST -design must match logo colors
Nice to have
• One or more pages that show more specific details/scope of each of the options presented (unless this is TMI and we can provide a URL
Should not have
• too much wordiness

```html
<!DOCTYPE html>
<html lang="en">
<head>
<meta charset="utf-8">
<title>Bramblet Roofing Co – Good / Better / Best Options</title>
<link href="https://fonts.googleapis.com/css2?family=Barlow:wght@400;500;600&family=Barlow+Condensed:wght@700&display=swap" rel="stylesheet">
<style>
  :root {
    --orange: #f26a36;
    --orange-deep: #e2592a;
    --brown: #5c524e;
    --ink: #2b2b2b;
    --page: #ffffff;
    --pattern-light: #f3f3f3;
    --pattern-mid: #e0e0e0;
    --stage: #d6d6d6;
  }
  * { box-sizing: border-box; margin: 0; padding: 0; }
  html, body {
    width: 1200px; height: 1200px; overflow: hidden;
    background: var(--stage);
  }
  .sheet {
    position: absolute; left: 225px; top: 69px;
    width: 748px; height: 1062px;
    background: var(--page);
    overflow: hidden;
  }
  .sheet-pattern {
    position: absolute; inset: 0;
    background: radial-gradient(ellipse at 50% 45%, var(--page) 25%, var(--pattern-light) 62%, var(--pattern-mid) 100%);
  }

  .brand {
    position: absolute; left: 0; right: 0; top: 118px;
    text-align: center;
    font-family: "Barlow Condensed", sans-serif;
    font-weight: 700;
    color: var(--orange);
    line-height: 1;
    text-transform: uppercase;
  }
  .brand-line { display: block; font-size: 100px; letter-spacing: 1px; }

  .option { position: absolute; top: 444px; width: 150px; }
  .option-1 { left: 77px; }
  .option-2 { left: 302px; }
  .option-3 { left: 526px; }

  .option-tab {
    width: 135px; height: 46px;
    border-top-right-radius: 24px;
    color: #fff;
    font-family: "Barlow", sans-serif;
    font-weight: 500;
    font-size: 22px;
    line-height: 46px;
    padding-left: 14px;
    letter-spacing: 0.5px;
  }
  .tab-dark { background: var(--brown); }
  .tab-orange { background: var(--orange-deep); }

  .option-ribbon { position: relative; width: 145px; height: 372px; }
  .option-ribbon svg { position: absolute; inset: 0; }
  .ribbon-orange { fill: var(--orange); }
  .ribbon-dark { fill: var(--brown); }
  .option-tier {
    position: absolute; left: 72px; top: 162px;
    transform: translate(-50%, -50%) rotate(-90deg);
    color: #fff;
    font-family: "Barlow", sans-serif;
    font-weight: 600;
    font-size: 112px;
    line-height: 1;
    white-space: nowrap;
  }

  .option-summary {
    position: absolute; top: 884px; width: 200px;
    text-align: center;
    font-family: "Barlow", sans-serif;
    font-size: 14px; line-height: 19px;
    color: var(--ink);
  }
  .summary-1 { left: 50px; }
  .summary-2 { left: 275px; }
  .summary-3 { left: 500px; }

  .footer-rule {
    position: absolute; left: 139px; top: 1006px;
    width: 471px; height: 16px;
    background: var(--orange);
  }
  .footer-block {
    position: absolute; left: 278px; top: 997px;
    width: 195px; height: 31px;
    background: var(--brown);
  }
</style>
</head>
<body>
  <main class="sheet">
    <div class="sheet-pattern" role="img" aria-label="Light grey geometric maze line pattern background"></div>

    <header class="brand">
      <span class="brand-line">Bramblet</span>
      <span class="brand-line">Roofing Co</span>
    </header>

    <section class="option option-1">
      <div class="option-tab tab-dark">OPTION 1</div>
      <div class="option-ribbon">
        <svg viewBox="0 0 145 372" width="145" height="372"><polygon class="ribbon-orange" points="0,0 145,0 145,340 72.5,372 0,340"/></svg>
        <span class="option-tier">Good</span>
      </div>
    </section>

    <section class="option option-2">
      <div class="option-tab tab-orange">OPTION 2</div>
      <div class="option-ribbon">
        <svg viewBox="0 0 145 372" width="145" height="372"><polygon class="ribbon-dark" points="0,0 145,0 145,340 72.5,372 0,340"/></svg>
        <span class="option-tier">Better</span>
      </div>
    </section>

    <section class="option option-3">
      <div class="option-tab tab-dark">OPTION 3</div>
      <div class="option-ribbon">
        <svg viewBox="0 0 145 372" width="145" height="372"><polygon class="ribbon-orange" points="0,0 145,0 145,340 72.5,372 0,340"/></svg>
        <span class="option-tier">Best</span>
      </div>
    </section>

    <p class="option-summary summary-1">Remove and replace<br>existing roof with new<br>shingle tier 1 quality</p>
    <p class="option-summary summary-2">Remove and replace<br>existing roof with new<br>shingle tier 2 quality and<br>better warranty</p>
    <p class="option-summary summary-3">Remove and replace<br>existing roof with new<br>highest quality shingle and<br>highest grade warranty</p>

    <div class="footer-rule"></div>
    <div class="footer-block"></div>
  </main>
</body>
</html>
```